Brivon Australia Dental

I need to update my website and design. I have some ideas in mind and would like to replicate the format from another website into my own. I need the website to be easy to edit (I have no prior wordpress exp) after the design is complete. Please visit https://thelittlenestcare.org.au/ for example of layout.
Target Market(s)
Parents and elder folks
Industry/Entity Type
Dental
Coding
Coded - Design and coding required
Number of Pages Required
4 page
Font styles to use
Sans Serif
Colors
0392cd
Requirements
Must have
- - Home, Services, About Us, News
- - Colours
- - Clear action from viewers
- - Location of business (able to change all the time)
- - Illustrations/ photos

```html
<!DOCTYPE html>
<html lang="en">
<head>
<meta charset="utf-8">
<title>Brivon Australia Dental</title>
<link href="https://fonts.googleapis.com/css2?family=Lato:wght@400;700;900&display=swap" rel="stylesheet">
<style>
:root{
  --blue:#0392cd;
  --blue-dark:#0a7fb3;
  --navy:#0b3550;
  --grey:#efefef;
  --white:#ffffff;
  --text:#444;
}
*{box-sizing:border-box;margin:0;padding:0}
html,body{width:1200px;height:5141px;overflow:hidden}
body{font-family:'Lato',sans-serif;color:var(--white);background:var(--white);position:relative}
.abs{position:absolute}
.band{position:absolute;left:0;width:1200px}
.btn{display:inline-block;background:#27b0ec;color:#fff;border-radius:20px;font-size:11px;font-weight:700;letter-spacing:.5px;text-align:center;line-height:38px;height:38px}
h2{font-weight:700;font-size:34px;letter-spacing:1px}
p{font-size:11px;line-height:1.5}
.photo{position:absolute}
.link-more{font-size:11px;font-weight:700;letter-spacing:.5px}
/* header */
.site-header{top:0;height:64px;background:var(--blue)}
.brand{left:224px;top:8px;font-size:28px;font-weight:700;color:#fff}
.brand-sub{left:224px;top:44px;font-size:9px;letter-spacing:2px;color:#dff3fc}
.search{left:492px;top:18px;width:324px;height:26px;border-radius:13px;background:#e8f4fa;color:var(--blue);font-size:11px;padding:7px 16px}
.phone-box{left:880px;top:14px;font-size:10px;font-weight:700}
.phone-box b{display:block;font-size:12px;margin-top:4px}
.main-nav{top:64px;height:26px;background:#1a9fd6;display:flex;justify-content:center;gap:34px;font-size:10px;font-weight:700;line-height:26px}
.hero{top:90px;height:586px;background:linear-gradient(120deg,#3f6f86,#7aa7b9 50%,#2a5873)}
.hero-title{top:290px;width:1200px;text-align:center;font-size:54px;font-weight:400}
.hero-text{top:368px;width:1200px;text-align:center;font-size:11px}
/* about */
.about{top:676px;height:382px}
.about-left{left:0;width:534px;height:382px;background:var(--blue)}
.about-right{left:534px;width:666px;height:382px;background:var(--grey);color:var(--text)}
/* sections generic */
.blue{background:var(--blue)}
.service-col{width:180px}
.service-col h3{font-size:13px;font-weight:700;line-height:1.6;margin-bottom:12px}
.service-col p{font-size:9px}
.news-card{position:absolute;top:3888px;width:232px;height:262px;background:#1c9ed8}
.news-card .img{height:112px}
.news-card h4{font-size:12px;margin:24px 12px 10px;font-weight:700}
.news-card p{font-size:9px;margin:0 12px}
.news-card .arrow{position:absolute;right:8px;bottom:8px;width:22px;height:22px;background:#0b3a55;display:flex;align-items:center;justify-content:center}
.field-label{font-size:9px;color:#fff}
.field{background:#fff;height:26px}
.site-footer{top:4850px;height:291px;background:var(--navy)}
.footer-col h5{font-size:11px;font-weight:700;margin-bottom:16px}
.footer-col p{font-size:9px;line-height:1.6}
.circle{display:inline-block;width:22px;height:22px;border-radius:50%;background:#1f8fd0;margin-right:22px}
</style>
</head>
<body>

<header class="band site-header">
  <div class="abs brand">Brivon</div>
  <div class="abs brand-sub">for a better smile</div>
  <div class="abs search">Search
    <svg class="abs" style="right:12px;top:6px" width="13" height="13" viewBox="0 0 13 13"><circle cx="5.5" cy="5.5" r="4" fill="none" stroke="#0392cd" stroke-width="1.5"/><line x1="8.5" y1="8.5" x2="12" y2="12" stroke="#0392cd" stroke-width="1.5"/></svg>
  </div>
  <div class="abs phone-box">Brivon Dental Australia<b>
    <svg width="10" height="10" viewBox="0 0 10 10" style="vertical-align:-1px"><path d="M2 0l2 2.5-1 1.5a6 6 0 0 0 3 3l1.5-1L10 8l-1.5 2C4 10 0 6 0 1.5z" fill="#fff"/></svg> 1300 555 014</b></div>
</header>
<nav class="band main-nav"><span>HOME</span><span>ABOUT US</span><span>SERVICE</span><span>OUR MISSION</span><span>NEWS</span><span>CONTACT US</span></nav>

<section class="band hero" role="img" aria-label="Photo of a mother and young daughter smiling while looking at a tablet">
</section>
<div class="abs hero-title">For a better smile</div>
<p class="abs hero-text">Brivon Mobile Dental is a group of Dental Professionals who strongly believes anyone and<br>anywhere can look healthy and fabulous with a bright Smile.</p>
<div class="abs btn" style="left:500px;top:418px;width:200px">BOOK AN APPOINTMENT!</div>

<section class="band about">
  <div class="abs about-left">
    <h2 class="abs" style="left:224px;top:100px">About Us</h2>
    <p class="abs" style="left:224px;top:176px;width:290px">Brivon Mobile Dental is a group of Dental Professionals who strongly believes anyone and anywhere can look healthy and fabulous with a bright Smile.</p>
    <div class="abs link-more" style="left:224px;top:246px">READ MORE...</div>
  </div>
  <div class="abs about-right">
    <p class="abs" style="left:24px;top:172px;width:400px">Call us on <b>1300 555 014</b> or Contact us to learn how your local educator can benefit and participate in this program! and how your Retirement Home can benefit and participate in this program!</p>
    <div class="abs btn" style="left:28px;top:244px;width:176px">BOOK AN APPOINTMENT!</div>
    <div class="abs btn" style="left:226px;top:244px;width:176px">CONTACT US</div>
    <div class="photo" style="left:410px;top:130px;width:240px;height:220px;background:linear-gradient(135deg,#e9ece8,#c8d6c6)" role="img" aria-label="Photo of a green leaf in a glass vase"></div>
  </div>
</section>

<section class="band" style="top:1058px;height:468px">
  <div class="photo" style="left:0;top:0;width:534px;height:468px;background:linear-gradient(135deg,#dfe3e6,#9aa3aa)" role="img" aria-label="Photo of a dental chair and lamp in a bright clinic"></div>
  <div class="abs blue" style="left:534px;top:0;width:666px;height:468px">
    <h2 class="abs" style="left:26px;top:80px">Our Service</h2>
    <p class="abs" style="left:26px;top:150px;width:400px">Using our state of the art technology, our professional mobile Dental Care Service is available where ever you are. From routine check ups to complex dentures, our team of enthusiastic Dentists and Therapists are happy to assist and resolve all your dental needs.</p>
    <div class="abs service-col" style="left:30px;top:274px"><h3>GROW TO<br>SMILE PROGRAM</h3><p>Our mobile services are performed within the spacious compounds of our State of the Art Mobile clinic.</p><div class="link-more" style="margin-top:12px">READ MORE...</div></div>
    <div class="abs" style="left:206px;top:272px;width:1px;height:146px;background:#fff"></div>
    <div class="abs service-col" style="left:254px;top:274px"><h3>BEAUTIFUL &amp;<br>RETIRED PROGRAM</h3><p>Our mobile services are performed within the spacious compounds of our State of the Art Mobile clinic.</p><div class="link-more" style="margin-top:12px">READ MORE...</div></div>
  </div>
</section>

<section class="band" style="top:1526px;height:470px;background:var(--grey)">
  <div class="photo" style="left:860px;top:170px;width:340px;height:300px;background:linear-gradient(180deg,#f2f2f0,#e0ddd8)" role="img" aria-label="Photo of a white chair by a desk"></div>
  <h2 class="abs" style="left:224px;top:60px;color:var(--blue)">Our Reviews</h2>
  <svg class="abs" style="left:222px;top:218px" width="18" height="32" viewBox="0 0 18 32"><path d="M16 2L3 16l13 14" fill="none" stroke="#0392cd" stroke-width="2"/></svg>
  <svg class="abs" style="left:956px;top:218px" width="18" height="32" viewBox="0 0 18 32"><path d="M2 2l13 14L2 30" fill="none" stroke="#0392cd" stroke-width="2"/></svg>
  <div class="photo" style="left:416px;top:160px;width:370px;height:204px;background:linear-gradient(135deg,#c7d5de,#5e7d92)" role="img" aria-label="Photo of a dentist with a young patient in the clinic"></div>
  <p class="abs" style="left:418px;top:380px;width:380px;color:var(--blue)">"Dr Hollis is very nice and fun to talk to. She makes my teeth feel strong and clean" -</p>
  <p class="abs" style="left:750px;top:410px;color:var(--blue)">Jonah.</p>
</section>

<section class="band" style="top:1996px;height:368px">
  <div class="abs blue" style="left:0;top:0;width:666px;height:368px">
    <h2 class="abs" style="left:222px;top:90px">Our Story</h2>
    <p class="abs" style="left:222px;top:162px;width:404px">Dr Maren Hollis and her team believes everyone deserves a beautiful Smile, whoever and where ever you may be. Practised most of her career in Sydney, she is determined by her philosophy and created a way to deliver exceptional Dental Care to other parts of Australia- without jeopardising the quality of her work.</p>
    <div class="abs btn" style="left:222px;top:268px;width:180px">BOOK AN APPOINTMENT!</div>
  </div>
  <div class="photo" style="left:666px;top:0;width:534px;height:368px;background:linear-gradient(135deg,#e8b3c2,#c98a9c)" role="img" aria-label="Photo of a mother hugging her laughing daughter"></div>
</section>

<section class="band" style="top:2364px;height:368px">
  <div class="abs" style="left:0;top:0;width:666px;height:368px;background:#fff">
    <div class="abs" style="left:200px;top:140px;font-size:72px;font-weight:700;color:var(--blue)">Brivon</div>
  </div>
  <div class="abs blue" style="left:666px;top:0;width:534px;height:368px">
    <h2 class="abs" style="left:20px;top:92px">Our Mission</h2>
    <p class="abs" style="left:24px;top:164px;width:270px">At Brivon we aim to put a beautiful Smile on your face. Our dedicated team of Professionals aim to deliver the best possible Dental Care to you and your organisation. We are here to ensure you live healthy, not to govern the way you live.</p>
    <div class="abs btn" style="left:26px;top:274px;width:180px">CONTACT US</div>
  </div>
</section>

<section class="band" style="top:2732px;height:368px">
  <div class="abs blue" style="left:0;top:0;width:666px;height:368px">
    <h2 class="abs" style="left:222px;top:92px">Our Team</h2>
    <p class="abs" style="left:222px;top:166px;width:400px">At Brivon, our team consists of qualified and trained Dentists, Therapists and Nurses with over a decade of experience in the industry. Our team of caring and supportive admin staff will ensure your your experience goes as smooth as possible.</p>
    <div class="abs btn" style="left:222px;top:270px;width:180px">CALL US</div>
  </div>
  <div class="photo" style="left:666px;top:0;width:534px;height:368px;background:linear-gradient(135deg,#b9c6cf,#4a6a80)" role="img" aria-label="Photo of a dentist examining a patient"></div>
</section>

<section class="band" style="top:3100px;height:590px;background:#fff">
  <h2 class="abs" style="left:222px;top:92px;color:var(--blue)">where we are located</h2>
  <div class="photo" style="left:0;top:150px;width:1200px;height:440px;background:linear-gradient(180deg,#eceff1,#e2e6e9)" role="img" aria-label="Street map of the clinic's neighbourhood"></div>
  <svg class="abs" style="left:608px;top:330px" width="16" height="22" viewBox="0 0 16 22"><path d="M8 0a8 8 0 0 1 8 8c0 6-8 14-8 14S0 14 0 8a8 8 0 0 1 8-8z" fill="#e53935"/><circle cx="8" cy="8" r="3" fill="#fff"/></svg>
  <div class="abs" style="left:302px;top:320px;width:266px;height:90px;background:#fff;box-shadow:0 2px 6px rgba(0,0,0,.2);color:var(--blue)">
    <div class="abs" style="left:20px;top:26px;font-size:26px;font-weight:700">Brivon</div>
    <div class="abs" style="left:128px;top:18px;width:1px;height:54px;background:#9bd"></div>
    <p class="abs" style="left:138px;top:20px;font-size:9px">Elmwood Public School<br>42 Carrow St, Elmwood NSW<br>2600, Australia</p>
  </div>
</section>

<section class="band" style="top:3690px;height:550px;background:linear-gradient(180deg,#0a7fb8,#0392cd)">
  <h2 class="abs" style="left:222px;top:90px">Our latest news</h2>
</section>
<article class="news-card" style="left:224px"><div class="img" role="img" aria-label="Photo of the mobile dental clinic van" style="background:linear-gradient(135deg,#c9dde8,#6d95ab)"></div><h4>PROFESSIONALISM</h4><p>Our actions do the talking. Our caring and passionate staff will meet all your dental needs to ensure you are comfortable during the procedure and leave our clinic with a Smile.</p><div class="arrow"><svg width="8" height="10" viewBox="0 0 8 10"><path d="M1 1l5 4-5 4" fill="none" stroke="#fff" stroke-width="2"/></svg></div></article>
<article class="news-card" style="left:482px"><div class="img" role="img" aria-label="Photo of a harbour town waterfront" style="background:linear-gradient(180deg,#9cc6e2,#3f7fa6)"></div><h4>HONESTY</h4><p>Our work is our purpose, our driving force. Our patients are our number one priority and we will help you through all your Dental needs.</p><div class="arrow"><svg width="8" height="10" viewBox="0 0 8 10"><path d="M1 1l5 4-5 4" fill="none" stroke="#fff" stroke-width="2"/></svg></div></article>
<article class="news-card" style="left:742px"><div class="img" role="img" aria-label="Photo of a child drawing with a green pencil" style="background:linear-gradient(135deg,#5a6a5e,#1f2d26)"></div><h4>EDUCATION</h4><p>Our purpose is to Educate anyone and everyone how to create and maintain their best Smile possible. We will like to guide you through your life journey.</p><div class="arrow"><svg width="8" height="10" viewBox="0 0 8 10"><path d="M1 1l5 4-5 4" fill="none" stroke="#fff" stroke-width="2"/></svg></div></article>

<section class="band" style="top:4240px;height:610px;background:#fff">
  <form class="abs blue" style="left:224px;top:96px;width:752px;height:436px">
    <div class="abs" style="left:0;top:42px;width:752px;text-align:center;font-size:17px;font-weight:700">Contact Us</div>
    <div class="abs field-label" style="left:94px;top:102px">First Name</div>
    <div class="abs field" style="left:94px;top:116px;width:272px"></div>
    <div class="abs field-label" style="left:382px;top:102px">Last Name</div>
    <div class="abs field" style="left:382px;top:116px;width:272px"></div>
    <div class="abs field-label" style="left:94px;top:158px">Email</div>
    <div class="abs field" style="left:94px;top:172px;width:560px"></div>
    <div class="abs field-label" style="left:94px;top:214px">Enquiry</div>
    <div class="abs field" style="left:94px;top:228px;width:560px;height:84px"></div>
    <div class="abs btn" style="left:320px;top:350px;width:128px;line-height:34px;height:34px;background:#27b0ec">SUBMIT</div>
  </form>
</section>

<footer class="band site-footer">
  <div class="abs brand" style="left:224px;top:36px;color:#1f9fd8">Brivon</div>
  <div class="abs" style="left:224px;top:72px;font-size:9px;letter-spacing:2px;color:#1f9fd8">for a better smile</div>
  <div class="abs footer-col" style="left:224px;top:124px">
    <h5><svg width="14" height="18" viewBox="0 0 16 22" style="vertical-align:-4px"><path d="M8 0a8 8 0 0 1 8 8c0 6-8 14-8 14S0 14 0 8a8 8 0 0 1 8-8z" fill="#1f9fd8"/><circle cx="8" cy="8" r="3" fill="#0b3550"/></svg> VISIT US</h5>
    <p>Elmwood Public School<br>42 Carrow St, Elmwood NSW<br>2600, Australia</p>
  </div>
  <div class="abs footer-col" style="left:444px;top:38px"><h5>LINKS</h5><p>HOME<br>ABOUT US<br>SERVICE<br>OUR STORY<br>OUR TEAM<br>OUR MISSION<br>NEWS<br>CONTACT US</p></div>
  <div class="abs footer-col" style="left:630px;top:38px"><h5>CONTACT US</h5>
    <p><span class="circle" style="width:14px;height:14px;margin:0"></span><br>hello@brivon.com.au<br><br><span class="circle" style="width:14px;height:14px;margin:0"></span><br>www.brivon.com.au<br><br><span class="circle" style="width:14px;height:14px;margin:0"></span><br>www.brivon.com.au</p></div>
  <div class="abs footer-col" style="left:824px;top:38px"><h5>FOLLOW US</h5>
    <div><span class="circle"></span><span class="circle"></span><span class="circle"></span></div>
    <p style="margin-top:26px">Imprint<br>Privacy Policy<br>Cookie Policy<br>Cookie Settings</p></div>
  <div class="abs" style="left:0;top:268px;width:1200px;text-align:center;font-size:9px">Copyright © 2019 Brivon Australia. All rights reserved.</div>
</footer>

</body>
</html>
```